Business Card - connecting 2 souls and beggining the journey of self discovery

Logo on the front
with tag line

On the back list of services and contact details

Seminars
workshops
Coaching
podcasts

Daniel Porthwick
Health & Wellbeing Life Coach
0491 372 815
daniel@wovenpathwellness.example
wovenpathwellness.example

Industry/Entity Type

Life Coaching

Contact Information for Business Card

I like the use of colour from the logo to be used. I'm not a fan of white.

Requirements
Must have
• My tagline: The journey home starts with you
Nice to have
• Use of colour that is in the mind body soul logo

```html
<!DOCTYPE html>
<html lang="en">
<head>
<meta charset="utf-8">
<title>Woven Path Wellness – Business Card</title>
<link rel="stylesheet" href="https://fonts.googleapis.com/css2?family=Open+Sans:wght@400;600;700&display=swap">
<style>
  :root {
    --stage: #1f1f21;
    --card-white: #ffffff;
    --ink: #3a3a3c;
    --ink-soft: #6d6d70;
    --purple: #7b3fa6;
    --violet: #9b54b0;
    --pink: #c77f9c;
    --yellow: #f2d34a;
    --lime: #8fcf4a;
    --green: #4cb37a;
    --orange: #f1a13d;
    --coral: #ef6f64;
    --front-text: #ffffff;
  }
  * { box-sizing: border-box; margin: 0; padding: 0; }
  html, body { width: 1200px; height: 1000px; overflow: hidden; }
  body {
    background: var(--stage);
    font-family: "Open Sans", Arial, sans-serif;
    position: relative;
  }
  .card {
    position: absolute;
    width: 600px;
    height: 343px;
    border-radius: 28px;
    overflow: hidden;
  }
  /* Front */
  .card-front {
    left: 100px;
    top: 110px;
    background:
      radial-gradient(circle at 98% 2%, var(--coral) 0, rgba(239,111,100,0) 32%),
      radial-gradient(circle at 85% 30%, var(--orange) 0, rgba(241,161,61,0) 35%),
      radial-gradient(circle at 95% 95%, var(--green) 0, rgba(76,179,122,0) 32%),
      radial-gradient(circle at 62% 78%, var(--yellow) 0, rgba(242,211,74,0) 30%),
      radial-gradient(circle at 40% 75%, var(--lime) 0, rgba(143,207,74,0) 34%),
      radial-gradient(circle at 45% 22%, var(--yellow) 0, rgba(242,211,74,0) 36%),
      radial-gradient(circle at 22% 40%, var(--pink) 0, rgba(199,127,156,0) 35%),
      linear-gradient(90deg, var(--violet) 0%, var(--violet) 18%, var(--pink) 35%, var(--lime) 60%, var(--orange) 100%);
  }
  .front-words {
    position: absolute;
    left: 150px;
    top: 62px;
    color: var(--front-text);
    font-size: 64px;
    font-weight: 400;
    line-height: 1;
    letter-spacing: 3px;
    text-align: center;
  }
  .front-brand {
    position: absolute;
    right: 26px;
    top: 206px;
    width: 206px;
    color: var(--front-text);
    text-align: left;
  }
  .front-brand .brand-name { font-size: 18px; font-weight: 600; letter-spacing: -0.3px; line-height: 1.2; white-space: nowrap; }
  .front-brand .tagline { font-size: 12.5px; font-weight: 400; line-height: 1.3; white-space: nowrap; }

  /* Back */
  .card-back {
    left: 500px;
    top: 540px;
    background: var(--card-white);
  }
  .tab {
    position: absolute;
    left: 0;
    top: 150px;
    width: 10px;
    height: 34px;
    background: var(--purple);
    border-radius: 0 4px 4px 0;
  }
  .identity { position: absolute; left: 36px; top: 140px; }
  .identity .person { font-size: 26px; font-weight: 700; color: var(--ink); line-height: 1.1; }
  .identity .role { font-size: 17px; font-weight: 600; color: var(--purple); }
  .brand-block {
    position: absolute;
    right: 34px;
    top: 34px;
    display: flex;
    align-items: center;
    gap: 10px;
  }
  .brand-dot {
    width: 34px; height: 34px; border-radius: 50%;
    background: var(--violet);
  }
  .brand-block .brand-name { font-size: 20px; font-weight: 600; color: var(--ink-soft); letter-spacing: -0.4px; }
  .services {
    position: absolute;
    right: 34px;
    top: 130px;
    text-align: right;
    font-size: 14px;
    color: var(--ink);
    letter-spacing: 0.4px;
    line-height: 1.3;
  }
  .contacts {
    position: absolute;
    left: 36px;
    bottom: 34px;
    list-style: none;
    font-size: 14px;
    color: var(--ink);
    line-height: 1.45;
  }
  .contacts li { display: flex; align-items: center; gap: 10px; }
  .contacts svg { width: 12px; height: 12px; fill: var(--purple); flex: none; }
  .contacts .accent { color: var(--purple); }
</style>
</head>
<body>
  <section class="card card-front" aria-label="Card front">
    <div class="front-words">MIND<br>BODY<br>SOUL</div>
    <div class="front-brand">
      <div class="brand-name">Woven Path Wellness</div>
      <div class="tagline">The journey home starts with you</div>
    </div>
  </section>

  <section class="card card-back" aria-label="Card back">
    <div class="tab"></div>
    <div class="brand-block">
      <span class="brand-dot"></span>
      <span class="brand-name">Woven Path Wellness</span>
    </div>
    <div class="identity">
      <div class="person">Daniel Porthwick</div>
      <div class="role">Life Coach</div>
    </div>
    <div class="services">
      SEMINARS | WORKSHOPS<br>COACHING | PODCASTS
    </div>
    <ul class="contacts">
      <li>
        <svg viewBox="0 0 12 12" aria-hidden="true"><path d="M3 0h6a1 1 0 0 1 1 1v10a1 1 0 0 1-1 1H3a1 1 0 0 1-1-1V1a1 1 0 0 1 1-1zm0 1.5v7.5h6V1.5zM6 10a.6.6 0 1 0 0 1.2A.6.6 0 0 0 6 10z"/></svg>
        0491 372 815
      </li>
      <li>
        <svg viewBox="0 0 12 12" aria-hidden="true"><path d="M0 2h12v1.2L6 7 0 3.2zM0 4.6l6 3.8 6-3.8V10H0z"/></svg>
        daniel@wovenpathwellness.example
      </li>
      <li>
        <svg viewBox="0 0 12 12" aria-hidden="true"><circle cx="6" cy="6" r="6"/><path d="M1 6h10M6 0.5v11" stroke="#fff" stroke-width="0.8"/></svg>
        <span>www.<span class="accent">wovenpathwellness</span>.example</span>
      </li>
    </ul>
  </section>
</body>
</html>
```